BRIMCOVE is a New Zealand based aerial imaging company performing mapping, surveying and videography

I would like a business card that is contemporary and clean. The font for the business name is called Gtec Technology and I would like to have the text "AERIAL IMAGING" under the "BRIMCOVE" name in a font similar to URW Gothic or another light modern font. Brimcove performs aerial imaging projects using a hexacopter UAV. Surveying and mapping with 3D Digital Elevation Models are a focus, I also produce aerial photographs and video's including post editing.

Target Market(s)

Industrial plant managers, Property owners, Event organisers.

Industry/Entity Type

Videography

Contact Information for Business Card

BRIMCOVE AERIAL IMAGING. Owner Reid Malloway. Cell: 021 7304169. P.O. Box 8316 Dunedin, New Zealand.

Font styles to use
Other font styles liked:
• Gtec Technology

Colors
9bcb3b
33a6d7
ec1f27

Requirements
Must have
• Modern professional look.
Nice to have
• Perhaps an aerial image of a landscape who's location is not identifiable. Maybe use included image of my hexacopter on the back of the card? Not compulsory though.
Should not have
• Clip Art style images.

```html
<!DOCTYPE html>
<html lang="en">
<head>
<meta charset="utf-8">
<title>Brimcove Aerial Imaging – Business Card</title>
<link rel="stylesheet" href="https://fonts.googleapis.com/css2?family=Poppins:wght@600&family=Questrial&display=swap">
<style>
  :root {
    --brand-green: #9bcb3b;
    --brand-blue: #33a6d7;
    --rule-grey: #d4d4d4;
    --card-white: #ffffff;
    --page-bg: #eeeeee;
  }
  * { margin: 0; padding: 0; box-sizing: border-box; }
  html, body {
    width: 1200px;
    height: 1000px;
    overflow: hidden;
    background: var(--page-bg);
  }
  .stage {
    position: relative;
    width: 1200px;
    height: 1000px;
  }
  .business-card {
    position: absolute;
    left: 179px;
    top: 221px;
    width: 839px;
    height: 467px;
    background: var(--card-white);
  }
  .holder {
    position: absolute;
    left: 0;
    width: 100%;
    text-align: center;
    color: var(--brand-green);
  }
  .holder-name {
    top: 117px;
    left: -2px;
    font-family: "Poppins", "Questrial", sans-serif;
    font-weight: 600;
    font-size: 39px;
    letter-spacing: -0.5px;
    line-height: 1;
  }
  .holder-role {
    top: 165px;
    left: 4px;
    font-family: "Questrial", sans-serif;
    font-size: 31px;
    line-height: 1;
  }
  .divider {
    position: absolute;
    left: 207px;
    top: 231px;
    width: 461px;
    height: 3px;
    background: var(--rule-grey);
  }
  .contact {
    position: absolute;
    left: 202px;
    top: 284px;
    font-family: "Questrial", sans-serif;
    font-size: 26px;
    line-height: 32px;
    color: var(--brand-blue);
    list-style: none;
    white-space: nowrap;
  }
</style>
</head>
<body>
  <main class="stage">
    <section class="business-card" aria-label="Business card">
      <h1 class="holder holder-name">REID MALLOWAY</h1>
      <p class="holder holder-role">Owner</p>
      <div class="divider"></div>
      <ul class="contact">
        <li class="contact-company">BRIMCOVE AERIAL IMAGING</li>
        <li class="contact-phone">Cell: 021 7304169</li>
        <li class="contact-address">P.O. Box 8316 Dunedin, New Zealand</li>
      </ul>
    </section>
  </main>
</body>
</html>
```